Broschüre für eine Unternehmensberatung
Lukas war sehr sehr zuvorkommend und hat uns ein hervorragendes Design geliefert. Wir sind sehr dankbar für die tolle Arbeit die er geleistet hat und freuen uns auf die zukünftigen Projekte. Lukas was very forthcoming and made a great design. We really appreciate his great work and are looking forward working with him again.
Zielgruppe
Unternehmen
Wir sind eine Unternehmensberatung, die sich auf Softwareentwicklung für den Public Sektor spezialisiert hat (www.kwl-beratung.de). Wir bieten für diesen Markt verschiedene Softwareprodukte an. Eines unserer Produkte für das diese Broschüre erstellt werden soll lautet velmo (www.velmo.de) und ist eine Webapplikation die sich an Lehrer und Schüler richtet.
Company
We are a consulting company, that is specialised in softwaredevelopment regarding the public sector (www.kwl-beratung.de). Our customers are administrations all over Germany, Austria and Swiss. We offer different products to the market. Our current product is named velmo (www.velmo.de) and its targetet towards teachers and their classes.
Aufgabenstellung
Bitte keine Designs mehr einreichen, wir haben uns für einen Designer entschieden. Wir bedanken uns bei Ihnen allen für Ihre Mühe.
Die Broschüre soll hochwertig wirken und clean aussehen.
Das Produkt und die Vorteile der Nutzung sollen hervorgehoben werden (Infotext Lernverlaufsdiagnostik-v3.docx). Es muss ersichtlich werden, dass der Leherer andere Informationen bekommt als die Schüler. Wir nennen dies die Lehreransicht (Screenshot Lehrer.docx) und die Schüleransicht ( velmo Schüler - Aufgabe Lesen Klasse 2.png; velmo Schüler - Begrüßung.png; velmo Schüler - Ergebnisanzeige.png) . Es wäre gut, wenn alle Screenshots für die Schüler verwendet werden könnten.
Es sollte ein A4 Folder mit 6 Seiten werden.
Please dont send us any more designs. We found the winning one already. We thank you all for your designs and the work you put in.
The brochure should look high quality and clean.
The benefits of the product and the screenshots should be focused on((Infotext Lernverlaufsdiagnostik-v3.docx)). the brochure has to show the diffrent clients for teachers ((Screenshot Lehrer.docx)) and students ( velmo Schüler - Aufgabe Lesen Klasse 2.png; velmo Schüler - Begrüßung.png; velmo Schüler - Ergebnisanzeige.png) .
We are looking for a A4 Folder Design (6 Sites)

```html
<!DOCTYPE html>
<html lang="de">
<head>
<meta charset="utf-8">
<title>Lernverlaufsdiagnostik – velmo</title>
<link href="https://fonts.googleapis.com/css2?family=Montserrat:wght@500;600;800&display=swap" rel="stylesheet">
<style>
  :root {
    --green: #8cc63f;
    --grey: #5a5a5a;
    --white: #ffffff;
    --screen-a: #e9ece0;
    --screen-b: #d8d3b8;
  }
  html, body {
    margin: 0;
    padding: 0;
    width: 1200px;
    height: 878px;
    overflow: hidden;
    background: var(--white);
    font-family: "Montserrat", sans-serif;
  }
  .page {
    position: relative;
    width: 1200px;
    height: 878px;
  }
  .brand {
    position: absolute;
    left: 1040px;
    top: 42px;
    display: flex;
    align-items: center;
    gap: 10px;
    color: var(--green);
    font-weight: 800;
    font-size: 30px;
  }
  .brand-dot {
    width: 30px;
    height: 30px;
    border-radius: 50%;
    background: var(--green);
  }
  .title {
    position: absolute;
    left: 86px;
    top: 52px;
    margin: 0;
    color: var(--green);
    font-weight: 800;
    font-size: 56px;
    letter-spacing: -0.5px;
  }
  .features {
    position: absolute;
    left: 93px;
    top: 0;
    margin: 0;
    padding: 0;
    list-style: none;
  }
  .feature {
    position: absolute;
    left: 0;
    width: 520px;
    display: flex;
    align-items: center;
  }
  .feature-num {
    flex: none;
    width: 32px;
    height: 32px;
    border-radius: 50%;
    background: var(--green);
    box-shadow: 0 0 0 2px var(--white), 0 0 0 4px var(--green);
    color: var(--white);
    font-weight: 600;
    font-size: 19px;
    display: flex;
    align-items: center;
    justify-content: center;
    margin-left: 2px;
  }
  .feature-text {
    margin-left: 20px;
    color: var(--grey);
    font-weight: 600;
    font-size: 20px;
    line-height: 1.1;
  }
  .feature-sub {
    display: block;
    color: var(--green);
    font-weight: 600;
    font-size: 14.5px;
    line-height: 1.2;
    margin-top: 2px;
  }
  .legend-row {
    display: flex;
    align-items: flex-start;
    gap: 8px;
    color: var(--green);
    font-size: 14.5px;
    line-height: 1.05;
  }
  .legend-row + .legend-row { margin-top: 4px; }
  .legend-dot, .legend-square {
    flex: none;
    width: 10px;
    height: 10px;
    background: var(--grey);
    margin-top: 3px;
  }
  .legend-dot { border-radius: 50%; }
  .teacher-view {
    position: absolute;
    left: 616px;
    top: 235px;
    width: 504px;
    height: 327px;
    background: linear-gradient(180deg, var(--screen-b) 0%, var(--screen-a) 18%, var(--white) 100%);
    border: 1px solid #d9d9d9;
  }
  .caption {
    position: absolute;
    left: 599px;
    top: 705px;
    width: 520px;
    margin: 0;
    color: #333;
    font-weight: 500;
    font-size: 15.5px;
    line-height: 1.25;
  }
  .caption-label { color: var(--green); }
</style>
</head>
<body>
<main class="page">
  <div class="brand"><span class="brand-dot"></span>velmo</div>

  <h1 class="title">Lernverlaufsdiagnostik</h1>

  <ol class="features">
    <li class="feature" style="top:266px"><span class="feature-num">1</span><span class="feature-text">Klassenauswahl</span></li>
    <li class="feature" style="top:313px"><span class="feature-num">2</span><span class="feature-text">Fachauswahl</span></li>
    <li class="feature" style="top:356px"><span class="feature-num">3</span><span class="feature-text">Funktionsauswahl:<span class="feature-sub">Lernverlaufskurven, Testzeitpunkte, Klassenliste</span></span></li>
    <li class="feature" style="top:403px"><span class="feature-num">4</span><span class="feature-text">Funktionsauswahl:<span class="feature-sub">Mail, Drucken, Einstellungen</span></span></li>
    <li class="feature" style="top:456px"><span class="feature-num">5</span><span class="feature-text">Schülerliste</span></li>
    <li class="feature" style="top:500px"><span class="feature-num">6</span><span class="feature-text">
      <span class="legend-row"><span class="legend-dot"></span>Punkte zeigen, welcher Test bearbeitet wurde</span>
      <span class="legend-row"><span class="legend-square"></span>Quadrate zeigen, welche Teilkompetenzen erreicht wurden</span>
    </span></li>
    <li class="feature" style="top:559px"><span class="feature-num">7</span><span class="feature-text">Ergebnisgraphik nach Teilkompetenzen</span></li>
    <li class="feature" style="top:606px"><span class="feature-num">8</span><span class="feature-text">Hinweise zu Fördermaßnahmen</span></li>
    <li class="feature" style="top:648px"><span class="feature-num">9</span><span class="feature-text">Anzeigeoptionen für:<span class="feature-sub">Normwerte, Mittelwerte, Hinweise zu<br>Förderempfehlungen</span></span></li>
  </ol>

  <div class="teacher-view" role="img" aria-label="Bildschirmansicht der Lehreransicht mit Schülerliste, Lernverlaufskurven und Förderhinweisen, nummeriert 1 bis 9"></div>

  <p class="caption"><span class="caption-label">Abbildung:</span> Darstellung des Lehrermenüs und der zentralen Funktionalitäten</p>
</main>
</body>
</html>
```